Digital content business needs banner ads

We sell content - if you need an article to put on your website or in a newsletter, you can purchase a ready made article from us and edit it to your liking to use straight away. This could be any kind of article, but this banner ad will be aimed at real estate agents. You can see the website (and the style of articles) here https://www.thebluelanternpost.com.au
The banner is meant to solve the problem of the front desk admin or agent trying to think of something to write to put in their email newsletter. This will save them time as they can just select an article from our library and use it (for a fee of course!).
Needs to have the words:
--------------------------------------------------
Find the next article for your newsletter
---------------------------------------------------
Some imagery would be good rather than plain text.
With a call to action like click here button or similar
Required sizes (or provide a set of standard sized ads):
728 x 90
970 x 250
300x250
Real Estate Agents

```html
<!DOCTYPE html>
<html lang="en">
<head>
<meta charset="utf-8">
<title>The Blue Lantern Post – Newsletter Article Banner Set</title>
<link rel="stylesheet" href="https://fonts.googleapis.com/css2?family=Oswald:wght@500;600;700&family=Roboto+Condensed:wght@400&display=swap">
<style>
  :root{
    --sky:#0aa3e4;
    --royal:#3f63b1;
    --navy:#1d2f5e;
    --ink:#1b1b1b;
    --paper:#ffffff;
    --photo-warm:#e9dcd4;
    --photo-grey:#c9c9c9;
  }
  *{box-sizing:border-box;margin:0;padding:0}
  html,body{width:1200px;height:1200px;overflow:hidden;background:var(--paper)}
  .sheet{position:relative;width:1200px;height:1200px;background:var(--paper)}

  .ad{position:absolute;overflow:hidden;background:var(--paper);box-shadow:0 2px 6px rgba(0,0,0,.18)}
  .ad__shapes{position:absolute;inset:0;width:100%;height:100%}
  .ad__photo{position:absolute}
  .ad__brand{position:absolute;display:flex;align-items:center;gap:4px;font-family:"Oswald",sans-serif;font-weight:600;color:var(--ink);white-space:nowrap;line-height:1}
  .ad__brand-mark{display:block;background:var(--sky)}
  .ad__headline{position:absolute;margin:0;font-weight:inherit}
  .ad__lead,.ad__title,.ad__accent{display:block;white-space:nowrap;line-height:1}
  .ad__lead{font-family:"Roboto Condensed",sans-serif;font-weight:400;color:var(--royal)}
  .ad__title,.ad__accent{font-family:"Oswald",sans-serif;font-weight:600;letter-spacing:-.01em;text-transform:uppercase}
  .ad__title{color:var(--royal)}
  .ad__accent{color:var(--sky)}
  .ad__query,.ad__call{position:absolute}
  .ad__phone{position:absolute;display:flex;align-items:center;justify-content:center;border:2px solid var(--royal);border-radius:999px;background:var(--paper);font-family:"Oswald",sans-serif;font-weight:500;color:var(--navy);white-space:nowrap;line-height:1}
  .ad__rule{position:absolute;height:1.5px;background:var(--royal)}

  /* 970 x 250 */
  .ad--billboard{left:259px;top:169px;width:664px;height:172px}
  .ad--billboard .ad__photo{left:0;top:0;width:280px;height:172px;background:linear-gradient(90deg,var(--photo-grey) 0%,var(--photo-warm) 40%,#f4f1ef 75%,rgba(255,255,255,0) 100%)}
  .ad--billboard .ad__brand{left:268px;top:24px;font-size:11px}
  .ad--billboard .ad__brand-mark{width:10px;height:10px}
  .ad--billboard .ad__headline{left:285px;top:52px}
  .ad--billboard .ad__lead{font-size:17px;margin-bottom:3px}
  .ad--billboard .ad__title{font-size:31px;margin-bottom:-2px}
  .ad--billboard .ad__accent{font-size:31px}
  .ad--billboard .ad__query{left:430px;top:12px;width:62px;height:122px}
  .ad--billboard .ad__call{left:516px;top:33px;width:90px;height:90px}
  .ad--billboard .ad__phone{left:500px;top:128px;width:123px;height:24px;font-size:15px}
  .ad--billboard .ad__rule{left:623px;top:139px;width:23px}

  /* 728 x 90 */
  .ad--leaderboard{left:177px;top:432px;width:854px;height:106px}
  .ad--leaderboard .ad__photo{left:0;top:0;width:300px;height:106px;background:linear-gradient(90deg,var(--photo-grey) 0%,var(--photo-warm) 35%,#f4f1ef 70%,rgba(255,255,255,0) 100%)}
  .ad--leaderboard .ad__brand{left:326px;top:17px;font-size:9px}
  .ad--leaderboard .ad__brand-mark{width:8px;height:8px}
  .ad--leaderboard .ad__headline{left:380px;top:35px}
  .ad--leaderboard .ad__lead{font-size:13px;margin-bottom:2px}
  .ad--leaderboard .ad__title{font-size:22px;margin-bottom:-2px}
  .ad--leaderboard .ad__accent{font-size:22px}
  .ad--leaderboard .ad__query{left:492px;top:7px;width:47px;height:91px}
  .ad--leaderboard .ad__call{left:564px;top:11px;width:74px;height:74px}
  .ad--leaderboard .ad__phone{left:657px;top:43px;width:148px;height:28px;font-size:19px}

  /* 300 x 250 */
  .ad--rectangle{left:351px;top:646px;width:505px;height:421px}
  .ad--rectangle .ad__photo{left:0;top:190px;width:330px;height:231px;background:linear-gradient(180deg,rgba(255,255,255,0) 0%,rgba(233,220,212,.7) 25%,var(--photo-warm) 60%,#ddd 100%)}
  .ad--rectangle .ad__photo-fade{position:absolute;inset:0;background:linear-gradient(90deg,rgba(255,255,255,0) 40%,#fff 100%)}
  .ad--rectangle .ad__brand{left:47px;top:36px;font-size:22px}
  .ad--rectangle .ad__brand-mark{width:18px;height:18px}
  .ad--rectangle .ad__headline{left:74px;top:108px}
  .ad--rectangle .ad__lead{font-size:23px;margin-bottom:4px}
  .ad--rectangle .ad__title{font-size:43px;margin-bottom:-3px}
  .ad--rectangle .ad__accent{font-size:43px}
  .ad--rectangle .ad__query{left:272px;top:54px;width:84px;height:169px}
  .ad--rectangle .ad__call{left:313px;top:201px;width:144px;height:144px}
  .ad--rectangle .ad__phone{left:288px;top:350px;width:181px;height:34px;font-size:23px}
</style>
</head>
<body>
<svg width="0" height="0" style="position:absolute" aria-hidden="true">
  <defs>
    <radialGradient id="btn-face" cx="50%" cy="35%" r="65%">
      <stop offset="0" stop-color="#3fb6f0"/>
      <stop offset=".6" stop-color="#0a79c9"/>
      <stop offset="1" stop-color="#07489a"/>
    </radialGradient>
    <linearGradient id="btn-ring" x1="0" y1="0" x2="0" y2="1">
      <stop offset="0" stop-color="#f2f2f2"/>
      <stop offset=".5" stop-color="#9b9b9b"/>
      <stop offset="1" stop-color="#4a4a4a"/>
    </linearGradient>
    <symbol id="call-button" viewBox="0 0 100 100">
      <ellipse cx="50" cy="96" rx="34" ry="3" fill="rgba(0,0,0,.18)"/>
      <circle cx="50" cy="50" r="48" fill="url(#btn-ring)"/>
      <circle cx="50" cy="50" r="41" fill="url(#btn-face)"/>
      <ellipse cx="50" cy="30" rx="30" ry="16" fill="rgba(255,255,255,.18)"/>
      <g transform="translate(37 19) scale(1.05)" fill="#dff3ff">
        <path d="M6.62 10.79c1.44 2.83 3.76 5.140 6.59 6.59l2.2-2.2c.27-.27.67-.36 1.02-.24 1.12.37 2.330.57 3.57.57.55 0 1 .45 1 1V20c0 .55-.45 1-1 1-9.39 0-17-7.610-17-17 0-.55.45-1 1-1h3.5c.55 0 1 .45 1 1 0 1.25.2 2.45.57 3.57.11.35.03.74-.25 1.02l-2.2 2.2z"/>
      </g>
      <g fill="none" stroke="#dff3ff" stroke-width="1.8" stroke-linecap="round">
        <path d="M53 24a8 8 0 0 1 8 8"/>
        <path d="M53 19a13 13 0 0 1 13 13"/>
        <path d="M53 14a18 18 0 0 1 18 18"/>
      </g>
      <text x="50" y="70" text-anchor="middle" font-family="Oswald, sans-serif" font-weight="500" font-size="14" fill="#ffffff">CALL US</text>
    </symbol>
    <symbol id="query-mark" viewBox="0 0 100 200" preserveAspectRatio="none">
      <path d="M14 56C14 24 34 8 56 8c26 0 38 18 38 40 0 30-36 40-36 72v18" fill="none" stroke="#0aa3e4" stroke-width="28"/>
      <rect x="44" y="152" width="32" height="46" fill="#3f63b1"/>
    </symbol>
  </defs>
</svg>

<main class="sheet">

  <section class="ad ad--billboard" aria-label="970 by 250 banner">
    <div class="ad__photo" role="img" aria-label="Photo of a business handshake above a model house resting on a contract with keys"></div>
    <svg class="ad__shapes" viewBox="0 0 664 172" preserveAspectRatio="none" aria-hidden="true">
      <polygon points="178,0 206,0 262,134" fill="var(--sky)"/>
      <polygon points="259,120 322,172 278,172" fill="var(--royal)"/>
      <polygon points="633,0 664,0 664,100" fill="var(--sky)"/>
      <polygon points="664,100 664,172 636,172" fill="var(--royal)"/>
    </svg>
    <div class="ad__brand"><span class="ad__brand-mark"></span>The Blue Lantern Post</div>
    <h2 class="ad__headline">
      <span class="ad__lead">Find the next article</span>
      <span class="ad__title">for your</span>
      <span class="ad__accent">newsletter</span>
    </h2>
    <svg class="ad__query" aria-hidden="true"><use href="#query-mark"/></svg>
    <svg class="ad__call" role="img" aria-label="Call us"><use href="#call-button"/></svg>
    <p class="ad__phone">+61 2 9000 4821</p>
    <span class="ad__rule"></span>
  </section>

  <section class="ad ad--leaderboard" aria-label="728 by 90 banner">
    <div class="ad__photo" role="img" aria-label="Photo of a business handshake above a model house resting on a contract"></div>
    <svg class="ad__shapes" viewBox="0 0 854 106" preserveAspectRatio="none" aria-hidden="true">
      <polygon points="223,0 248,0 289,99" fill="var(--sky)"/>
      <polygon points="279,73 317,106 289,106" fill="var(--royal)"/>
      <polygon points="813,0 854,0 826,62" fill="var(--sky)"/>
      <polygon points="854,6 854,106 816,106" fill="var(--royal)"/>
    </svg>
    <div class="ad__brand"><span class="ad__brand-mark"></span>The Blue Lantern Post</div>
    <h2 class="ad__headline">
      <span class="ad__lead">Find the next article</span>
      <span class="ad__title">for your</span>
      <span class="ad__accent">newsletter</span>
    </h2>
    <svg class="ad__query" aria-hidden="true"><use href="#query-mark"/></svg>
    <svg class="ad__call" role="img" aria-label="Call us"><use href="#call-button"/></svg>
    <p class="ad__phone">+61 2 9000 4821</p>
  </section>

  <section class="ad ad--rectangle" aria-label="300 by 250 banner">
    <svg class="ad__shapes" viewBox="0 0 505 421" preserveAspectRatio="none" aria-hidden="true">
      <polygon points="352,0 505,0 505,203" fill="var(--sky)"/>
      <polygon points="433,114 505,204 505,295" fill="var(--royal)"/>
    </svg>
    <div class="ad__photo" role="img" aria-label="Photo of a business handshake above a model house resting on a contract with keys"><span class="ad__photo-fade"></span></div>
    <div class="ad__brand"><span class="ad__brand-mark"></span>The Blue Lantern Post</div>
    <h2 class="ad__headline">
      <span class="ad__lead">Find the next article</span>
      <span class="ad__title">for your</span>
      <span class="ad__accent">newsletter</span>
    </h2>
    <svg class="ad__query" aria-hidden="true"><use href="#query-mark"/></svg>
    <svg class="ad__call" role="img" aria-label="Call us"><use href="#call-button"/></svg>
    <p class="ad__phone">+61 2 9000 4821</p>
  </section>

</main>
</body>
</html>
```